Store Front Signage for an Upscale Cake & Dessert Bakery

We need a design for store front windows. We are a 12 year old bakery specializing in cakes, cupcakes, cookies, pies, and other desserts. We recently moved to a high traffic location.. and we would like to boost our visual presence; we can be seen from the main road but are competing with other businesses for attention. Attached is a photo of our store front with posters but this signage will be for window film for the entire window span. (see the store front to the left of the photo to see the green and yellow as a film example)
Our logo and store sign (not like in photo, that is showing more red) are in shades of pink. The most visible part of the signage is in the upper third to upper half of the 60" panels.
The signs in the window currently say Life's Short. Eat Cake.
We now use Enjoy Life. Eat Cake.
The design should span all the windows and door -- this can be individual panels or one design that covers all panels. I have pink and greys chosen but please DO NOT let this constrain you. The inside of the bakery has grey floors and walls. white cabinetry, black granite countertops. The only thing with color is the baked goods and display cakes, pictures of cakes, the logo and menu and employee shirts.

Target Market(s)

we are located at a busy intersection --- we would like to capture the attention of people in cars as they pass by and entice them to stop in

Font styles to use
Serif
Sans Serif

Colors
d3d3d3
757575
ffffff
e24197
e667a6
eea4c8
f9d9e8

Requirements
Must have
• I would like the design to be easily discernible at the road way that is about 75 feet from store front. If you look at the photos I provide, note that the font size that is easily readable from the road are the ones in the top panes (although the shadow from the building makes them difficult to see -- the best visibility is the top 1/3 of the 60" panels.
Nice to have
• would like to have some non-photo graphics of a cake ( like a birthday cake), tiered cake, cupcakes, and cookies or pie for the panels --- but DO NOT let this constrain you. I need something to grab attention while cars are stopped at the nearby traffic light.
• If this design works well... I will be changing the panel on a seasonal basis
Should not have
• words that cannot be read from a distance.

```html
<!DOCTYPE html>
<html lang="en">
<head>
<meta charset="utf-8">
<title>Rosabelle's Storefront Window Film</title>
<link rel="stylesheet" href="https://fonts.googleapis.com/css2?family=Poppins:ital,wght@0,700;0,800;1,700;1,800&display=swap">
<style>
  :root {
    --pink: #e24197;
    --pink-soft: #e667a6;
    --pink-light: #eea4c8;
    --black: #0b0b0c;
    --frame: #a6a6a6;
    --frame-edge: #8a8a8a;
    --white: #ffffff;
    --page: #ffffff;
  }
  * { box-sizing: border-box; margin: 0; padding: 0; }
  html, body {
    width: 1200px; height: 1200px; overflow: hidden;
    background: var(--page);
    font-family: "Poppins", sans-serif;
  }
  .storefront {
    position: absolute; left: 19px; top: 317px;
    width: 1162px; height: 562px;
    background: var(--frame);
    outline: 1px solid var(--frame-edge);
  }
  .transom {
    position: absolute; top: 0; width: 235px; height: 147px;
    background: var(--pink);
  }
  .headline {
    position: absolute; left: 0; right: 0; top: 72px;
    text-align: center; color: var(--white);
    font-weight: 800; font-style: italic; font-size: 62px; line-height: 1;
    letter-spacing: -1px;
  }
  .pane {
    position: absolute; top: 157px; width: 235px; height: 296px;
    background: var(--black); overflow: hidden;
  }
  .drip-band {
    position: absolute; left: 0; top: 0; width: 100%; height: 96px;
    background: linear-gradient(180deg, var(--pink) 0%, var(--pink) 25%, var(--pink-light) 52%, var(--black) 100%);
  }
  .pane-copy {
    position: absolute; left: 0; right: 0; top: 88px;
    color: var(--white); font-weight: 800; font-style: italic;
    line-height: 1.05;
  }
  .line {
    display: inline-block;
    border-bottom: 1px solid var(--pink);
    padding-bottom: 2px;
  }
  .sm { font-size: 27px; }
  .md { font-size: 34px; }
  .gap { height: 18px; }
  .dots {
    position: absolute; top: 462px; width: 235px; height: 100px;
    background:
      radial-gradient(ellipse at 50% 20%, rgba(226,65,151,.75), rgba(226,65,151,.25) 55%, rgba(11,11,12,0) 85%),
      var(--black);
    border-bottom: 2px solid var(--pink);
  }
  .door {
    position: absolute; left: 493px; top: 0; width: 176px; height: 562px;
  }
  .door-top {
    position: absolute; left: 0; top: 0; width: 176px; height: 147px;
    background: var(--pink);
  }
  .door-frame {
    position: absolute; left: 0; top: 157px; width: 176px; height: 405px;
    background: var(--frame);
    border-left: 1px solid var(--frame-edge); border-right: 1px solid var(--frame-edge);
  }
  .door-glass {
    position: absolute; left: 23px; top: 24px; width: 130px; height: 345px;
    background: var(--black); overflow: hidden;
  }
  .door-glass .drip-band { height: 48px; }
  .door-info {
    position: absolute; left: 0; right: 0; top: 78px;
    text-align: center; font-style: italic; font-weight: 700;
  }
  .shop-name {
    color: var(--pink-soft); font-weight: 800; font-size: 13px; letter-spacing: .5px;
    margin-bottom: 20px;
  }
  .hours { font-size: 9px; line-height: 1.2; }
  .hours .label { color: var(--white); }
  .hours .time, .hours .title { color: var(--pink-soft); }
  .hours .spacer { height: 12px; }
</style>
</head>
<body>
<div class="storefront">
  <div class="transom" style="left:0"><div class="headline">Enjoy</div></div>
  <div class="transom" style="left:247px"><div class="headline">Life.</div></div>
  <div class="transom" style="left:680px"><div class="headline">Eat</div></div>
  <div class="transom" style="left:927px"><div class="headline">Cake.</div></div>

  <div class="pane" style="left:0">
    <div class="drip-band" role="img" aria-label="Pink icing drip band flowing into black"></div>
    <div class="pane-copy" style="padding-left:28px">
      <div class="sm"><span class="line">Custom</span></div>
      <div class="md">Cakes</div>
      <div class="gap"></div>
      <div class="md">Holiday</div>
      <div class="sm"><span class="line">Desserts</span></div>
    </div>
  </div>

  <div class="pane" style="left:247px">
    <div class="drip-band" role="img" aria-label="Pink icing drip band flowing into black"></div>
    <div class="pane-copy" style="text-align:center">
      <div class="md"><span class="line">Order</span></div>
      <div class="md">Online</div>
      <div class="gap"></div>
      <div style="font-size:21px;line-height:1.05">Rosabelles<br><span class="line" style="padding-left:92px">.com</span></div>
    </div>
  </div>

  <div class="pane" style="left:680px">
    <div class="drip-band" role="img" aria-label="Pink icing drip band flowing into black"></div>
    <div class="pane-copy" style="padding-left:44px">
      <div class="sm">Next day</div>
      <div class="md"><span class="line">Pick-up</span></div>
      <div class="gap"></div>
      <div class="md"><span class="line">Delivery</span></div>
      <div class="sm" style="padding-left:8px">Available</div>
    </div>
  </div>

  <div class="pane" style="left:927px">
    <div class="drip-band" role="img" aria-label="Pink icing drip band flowing into black"></div>
    <div class="pane-copy" style="text-align:center">
      <div class="sm"><span class="line">Cupcakes</span></div>
      <div class="md"><span class="line">Cookies</span></div>
      <div style="font-size:52px;line-height:1">&amp;</div>
      <div class="md" style="font-size:38px"><span class="line">Sweets</span></div>
    </div>
  </div>

  <div class="dots" style="left:0" role="img" aria-label="Pink halftone dot pattern fading into black"></div>
  <div class="dots" style="left:247px" role="img" aria-label="Pink halftone dot pattern fading into black"></div>
  <div class="dots" style="left:680px" role="img" aria-label="Pink halftone dot pattern fading into black"></div>
  <div class="dots" style="left:927px" role="img" aria-label="Pink halftone dot pattern fading into black"></div>

  <div class="door">
    <div class="door-top"></div>
    <div class="door-frame">
      <div class="door-glass">
        <div class="drip-band" role="img" aria-label="Pink icing drip band flowing into black"></div>
        <div class="door-info">
          <div class="shop-name">ROSABELLE'S</div>
          <div class="hours">
            <div class="title">Hours:</div>
            <div class="label">Monday - Saturday</div>
            <div class="time">8.00 am - 10.00 pm</div>
            <div class="spacer"></div>
            <div class="label">Sunday</div>
            <div class="time">11.00 am - 5.00 pm</div>
          </div>
        </div>
      </div>
    </div>
  </div>
</div>
</body>
</html>
```